Thornfield Marsh, LLC Website

We are a small law firm in need of a website that contains the following:
1. Attractive main page
2. About us/attorney info for three people: Leonard Thornfield (attorney), Brent Marsh (attorney), and Melinda Carrow (legal assistant). We have bio's ready to submit.
3. Blog/video page. We'd like to post blogs and videos to help drive traffic
4. Multidistrict Litigation and Class Actions page, where we post information regarding active MDLs and Class actions that we are doing intake on.
Updates

Can you also please use the color "gold" in the design and logo? Thanks.

Industry/Entity Type

Legal

Coding

Coded - Design and coding required

Number of Pages Required

1 page

Colors
0054AA
0677BA
7BADD7
CADEEF
E8F1F8

Requirements
Must have
• 1. Attractive main page 2. About us/attorney info for three people: Leonard Thornfield (attorney), Brent Marsh (attorney), and Melinda Carrow (legal assistant). We have bio's ready to submit. 3. Blog/video page. We'd like to post blogs and videos to help drive traffic 4. Multidistrict Litigation and Class Actions page, where we post information regarding active MDLs and Class actions that we are doing intake on.

```html
<!DOCTYPE html>
<html lang="en">
<head>
<meta charset="utf-8">
<title>Thornfield Marsh, LLC — Class Action &amp; MDL Lawyers</title>
<link href="https://fonts.googleapis.com/css2?family=Poppins:wght@400;500;600;700;800&display=swap" rel="stylesheet">
<style>
:root{
  --blue:#1aa5f6;
  --navy:#0a1a8a;
  --navy-deep:#07136b;
  --ink:#111111;
  --text:#333333;
  --white:#ffffff;
  --line:#e3e6ee;
  --sky:#cadeef;
}
*{box-sizing:border-box;margin:0;padding:0}
html,body{width:1200px;height:3906px;overflow:hidden}
body{position:relative;font-family:'Poppins',sans-serif;color:var(--text);background:var(--white)}
.abs{position:absolute}
.btn{position:absolute;display:flex;align-items:center;justify-content:center;font-size:11px;font-weight:600;text-transform:uppercase;letter-spacing:.2px;text-decoration:none}
.btn-solid{background:var(--blue);color:var(--white)}
.btn-outline{border:1.5px solid var(--navy);color:var(--ink);background:var(--white)}
.btn-navy{background:var(--navy);color:var(--white)}
.photo{position:absolute}

/* logo */
.logo{position:absolute;display:flex;align-items:center;gap:10px}
.logo-mark{width:34px;height:34px;background:var(--navy)}
.logo-name{font-weight:700;color:var(--navy);font-size:18px;letter-spacing:-.2px;white-space:nowrap}

/* header */
.nav{position:absolute;top:36px;left:372px;display:flex;gap:26px;font-size:11.5px;font-weight:500;color:var(--ink);text-transform:uppercase}
.nav-home{width:12px;height:12px}

/* hero */
.hero-title{left:92px;top:255px;font-size:57px;line-height:1;font-weight:800;color:var(--ink);letter-spacing:-.5px}
.hero-copy{left:92px;top:432px;width:420px;font-size:13px;line-height:1.5;color:var(--ink)}
.hero-frame{left:538px;top:323px;width:430px;height:361px;border:7px solid var(--navy);border-right:none;border-top:none}
.hero-frame::before{content:"";position:absolute;left:0;top:0;width:28px;height:7px;background:var(--navy)}
.hero-photo{left:566px;top:85px;width:634px;height:575px;background:linear-gradient(160deg,#a9c8e6 0%,#d9dfe4 40%,#8a8a86 75%,#4c4a46 100%)}

/* trusted */
.tile{position:absolute}
.trusted-title{left:611px;top:808px;font-size:33px;line-height:1.15;font-weight:800;color:var(--ink);letter-spacing:-.3px}
.trusted-copy{left:611px;top:893px;width:465px;font-size:12.5px;line-height:1.55;color:var(--ink)}
.trusted-copy p+p{margin-top:17px}

/* practice */
.section-title{font-size:33px;font-weight:800;color:var(--ink);letter-spacing:-.3px;text-align:center}
.explore{left:951px;top:1193px;font-size:11px;font-weight:600;color:var(--ink);text-decoration:underline;text-transform:uppercase}
.practice-card{position:absolute;top:1271px;width:245px;height:262px}
.practice-photo{position:absolute;left:0;top:0;width:245px;height:239px}
.practice-icon{position:absolute;left:96px;top:-20px;width:52px;height:42px;background:var(--blue);display:flex;align-items:center;justify-content:center}
.practice-label{position:absolute;left:12px;top:208px;width:221px;height:54px;background:var(--white);box-shadow:0 4px 14px rgba(0,0,0,.12);display:flex;align-items:center;justify-content:center;text-align:center;font-size:10.5px;line-height:1.2;font-weight:700;color:var(--ink);text-transform:uppercase}

/* team */
.team-band{left:0;top:1510px;width:1200px;height:553px;background:var(--navy)}
.team-deco{left:50px;top:1560px;width:320px;height:503px;background:linear-gradient(180deg,rgba(60,90,200,.35),rgba(40,70,180,.18));clip-path:polygon(30% 0,55% 0,70% 20%,80% 45%,70% 100%,10% 100%,20% 55%,25% 20%)}
.team-title{left:92px;top:1712px;font-size:33px;line-height:1.13;font-weight:800;color:var(--white);letter-spacing:-.3px}
.team-card{position:absolute;top:1646px;width:221px;height:316px;background:var(--white)}
.team-photo{position:absolute;left:0;top:0;width:221px;height:247px}
.team-name{position:absolute;left:0;top:266px;width:100%;text-align:center;font-size:12px;font-weight:700;color:var(--ink);text-transform:uppercase}
.team-role{position:absolute;left:0;top:282px;width:100%;text-align:center;font-size:12px;color:var(--ink)}

/* insights */
.insight-sub{left:250px;top:2211px;width:700px;text-align:center;font-size:12.5px;line-height:1.55;color:var(--ink)}
.insight-photo{position:absolute;top:2265px;width:501px;height:331px}
.insight-caption{position:absolute;top:2622px;width:501px;text-align:center;font-size:18px;font-weight:700;color:var(--ink);text-transform:uppercase;letter-spacing:-.2px}
.play{left:832px;top:2412px;width:40px;height:40px;border-radius:50%;background:rgba(20,20,20,.55);display:flex;align-items:center;justify-content:center}

/* ongoing */
.ongoing-frame{left:306px;top:2988px;width:275px;height:228px;border:7px solid var(--navy);border-top:none;border-left:none}
.ongoing-frame::before{content:"";position:absolute;right:-7px;top:-14px;width:7px;height:14px;background:var(--navy)}
.ongoing-photo{left:96px;top:2791px;width:462px;height:405px;background:linear-gradient(135deg,#5b5247 0%,#b9b0a4 45%,#e9e3da 70%,#8f7a63 100%)}
.ongoing-title{left:636px;top:2855px;font-size:33px;line-height:1.15;font-weight:800;color:var(--ink);letter-spacing:-.3px}
.ongoing-copy{left:637px;top:2950px;width:470px;font-size:12.5px;line-height:1.55;color:var(--ink)}
.ongoing-list{left:637px;top:3016px;list-style:none;font-size:12.5px;line-height:1.5;color:var(--ink)}
.ongoing-list li{display:flex;align-items:center;gap:7px}

/* cta */
.footer-band{left:0;top:3478px;width:1200px;height:428px;background:var(--navy)}
.cta{left:99px;top:3300px;width:1005px;height:221px;background:var(--blue);overflow:hidden}
.cta-title{left:60px;top:50px;font-size:27px;line-height:1.18;font-weight:800;color:var(--white);text-transform:uppercase;letter-spacing:-.2px}
.cta-copy{left:60px;top:110px;width:460px;font-size:12px;line-height:1.5;color:var(--white)}

/* footer */
.footer-nav{left:103px;top:3710px;display:flex;gap:30px;font-size:12.5px;color:var(--white)}
.footer-rule-left{left:60px;top:3742px;width:445px;height:1px;background:rgba(255,255,255,.25)}
.contact-title{left:614px;top:3627px;font-size:18px;font-weight:800;color:var(--white);text-transform:uppercase}
.contact-list{left:617px;top:3655px;list-style:none;font-size:12.5px;line-height:1.72;color:var(--white)}
.contact-list li{display:flex;align-items:center;gap:6px}
.social{position:absolute;top:3668px;width:34px;height:34px;border-radius:50%;border:1.5px solid rgba(255,255,255,.3)}
.footer-rule{left:92px;top:3797px;width:1010px;height:1px;background:rgba(255,255,255,.25)}
.legal{left:250px;top:3822px;width:700px;text-align:center;font-size:12.5px;line-height:1.7;color:var(--white)}
.to-top{left:1133px;top:3773px;width:38px;height:38px;background:var(--blue);display:flex;align-items:center;justify-content:center}
</style>
</head>
<body>

<!-- header -->
<header>
  <div class="logo" style="left:92px;top:22px">
    <span class="logo-mark"></span>
    <span class="logo-name">THORNFIELD MARSH, LLC</span>
  </div>
  <nav class="nav">
    <svg class="nav-home" viewBox="0 0 12 12"><path d="M6 1 1 5.5h1.5V11h2.8V7.5h1.4V11h2.8V5.5H11z" fill="#1aa5f6"/></svg>
    <span>About</span><span>Legal Team</span><span>Blog &amp; Videos</span><span>MDLs &amp; Class Actions</span><span>Contact</span>
  </nav>
  <a class="btn btn-solid" style="left:940px;top:23px;width:165px;height:42px">Free Consultation</a>
</header>

<!-- hero -->
<section>
  <div class="abs hero-frame"></div>
  <div class="photo hero-photo" role="img" aria-label="Classical courthouse columns and statues against a cloudy sky"></div>
  <h1 class="abs hero-title">JUSTICE.<br>DEDICATION.<br>RESULTS.</h1>
  <p class="abs hero-copy">Experienced legal professionals fighting for your rights in class action and multidistrict litigation cases.</p>
  <a class="btn btn-solid" style="left:92px;top:482px;width:137px;height:43px">Meet Our Team</a>
  <a class="btn btn-outline" style="left:235px;top:482px;width:150px;height:43px">See Active Cases</a>
</section>

<!-- trusted -->
<section>
  <div class="tile" style="left:126px;top:822px;width:135px;height:234px;background:linear-gradient(180deg,#6b5a48,#e8e4dc 45%,#1e1e1e)" role="img" aria-label="Laptop on a desk beside a stone wall"></div>
  <div class="tile" style="left:267px;top:784px;width:135px;height:100px;background:linear-gradient(180deg,#7a6450,#2b2b2b)" role="img" aria-label="Attorney portrait, upper section"></div>
  <div class="tile" style="left:267px;top:891px;width:135px;height:235px;background:linear-gradient(180deg,#2a2a2a,#111)" role="img" aria-label="Attorney in a suit working on a phone"></div>
  <div class="tile" style="left:408px;top:746px;width:135px;height:235px;background:linear-gradient(180deg,#6f6150,#1f1f22)" role="img" aria-label="Attorney in a suit, side view"></div>
  <div class="tile" style="left:408px;top:988px;width:135px;height:101px;background:linear-gradient(180deg,#3a3a3a,#d8d8d8)" role="img" aria-label="Coffee cup on a desk"></div>
  <h2 class="abs trusted-title">YOUR TRUSTED LEGAL<br>TEAM FOR COMPLEX CASES</h2>
  <div class="abs trusted-copy">
    <p>At <strong>Thornfield &amp; Marsh Law Group</strong>, we specialize in representing individuals and families impacted by corporate negligence, unsafe products, and deceptive practices. We combine personal attention with national-level legal experience, and we're here to make sure your voice is heard.</p>
    <p>Whether you're exploring a class action lawsuit or looking for support in a multidistrict litigation case, our team brings commitment and clarity to every client we serve.</p>
  </div>
</section>

<!-- practice areas -->
<section>
  <h2 class="abs section-title" style="left:0;top:1184px;width:1200px">PRACTICE AREAS</h2>
  <a class="abs explore">Explore Practice Areas</a>
</section>

<!-- team band -->
<section>
  <div class="abs team-band"></div>
  <div class="abs team-deco" role="img" aria-label="Faint Lady Justice statue silhouette"></div>
  <h2 class="abs team-title">MEET THE<br>TEAM BEHIND<br>THE MISSION</h2>
  <a class="btn btn-solid" style="left:92px;top:1838px;width:138px;height:43px">View Full Bios</a>

  <div class="team-card" style="left:422px">
    <div class="team-photo" style="background:linear-gradient(180deg,#e8e4dc,#b6a08a 55%,#1c1c1c)" role="img" aria-label="Portrait of Leonard Thornfield"></div>
    <div class="team-name">Leonard Thornfield</div>
    <div class="team-role">Attorney at Law</div>
  </div>
  <div class="team-card" style="left:652px">
    <div class="team-photo" style="background:linear-gradient(180deg,#2c2c2c,#6a5446 50%,#b9c8dc)" role="img" aria-label="Portrait of Brent Marsh"></div>
    <div class="team-name">Brent Marsh</div>
    <div class="team-role">Attorney at Law</div>
  </div>
  <div class="team-card" style="left:883px">
    <div class="team-photo" style="background:linear-gradient(180deg,#d3d8de,#b79a86 50%,#1a1a1e)" role="img" aria-label="Portrait of Melinda Carrow"></div>
    <div class="team-name">Melinda Carrow</div>
    <div class="team-role">Legal Assistant</div>
  </div>
</section>

<!-- practice cards (overlap band) -->
<section>
  <div class="practice-card" style="left:92px">
    <div class="practice-photo" style="background:linear-gradient(135deg,#e9d6a8,#a5814d 55%,#3a2b18)" role="img" aria-label="Courthouse columns in warm light"></div>
    <div class="practice-icon"><svg width="20" height="18" viewBox="0 0 20 18" fill="none" stroke="#fff" stroke-width="1.4"><path d="M10 2v14M4 4h12M6 16h8M4 4l-3 6h6zM16 4l-3 6h6z"/></svg></div>
    <div class="practice-label">Multidistrict<br>Litigation (MDLs)</div>
  </div>
  <div class="practice-card" style="left:347px">
    <div class="practice-photo" style="background:linear-gradient(135deg,#d6b27a,#5b3f24 60%,#2a1a10)" role="img" aria-label="Wooden gavel on a desk"></div>
    <div class="practice-icon"><svg width="18" height="20" viewBox="0 0 18 20" fill="none" stroke="#fff" stroke-width="1.4"><rect x="2" y="2" width="12" height="16"/><path d="M5 7h6M5 10h6M5 13h3"/></svg></div>
    <div class="practice-label">Class Action<br>Lawsuits</div>
  </div>
  <div class="practice-card" style="left:602px">
    <div class="practice-photo" style="background:linear-gradient(135deg,#3a3a3a,#1a1a1a 60%,#8a6a2a)" role="img" aria-label="Consumer protection book with a gavel"></div>
    <div class="practice-icon"><svg width="18" height="20" viewBox="0 0 18 20" fill="none" stroke="#fff" stroke-width="1.4"><path d="M9 2 3 4.5v5c0 4 3 7 6 8.5 3-1.5 6-4.5 6-8.5v-5z"/><path d="M6 10l2 2 4-4"/></svg></div>
    <div class="practice-label">Consumer<br>Protection</div>
  </div>
  <div class="practice-card" style="left:857px">
    <div class="practice-photo" style="background:linear-gradient(135deg,#1e5aa0,#c89a5a 40%,#eeeeee 70%)" role="img" aria-label="Mass tort document with a gavel"></div>
    <div class="practice-icon"><svg width="16" height="20" viewBox="0 0 16 20" fill="none" stroke="#fff" stroke-width="1.4"><rect x="3" y="6" width="10" height="12" rx="1"/><path d="M6 6V3h4v3M8 9v6M5 12h6"/></svg></div>
    <div class="practice-label">Mass Torts &amp;<br>Injury Claims</div>
  </div>
</section>

<!-- insights -->
<section>
  <h2 class="abs section-title" style="left:0;top:2162px;width:1200px">INSIGHTS, UPDATES &amp; LEGAL RESOURCES</h2>
  <p class="abs insight-sub">Stay informed with our latest blog posts and legal briefings. We break down complex issues and keep you up-to-date on the cases that matter.</p>
  <div class="insight-photo" style="left:92px;background:linear-gradient(180deg,#dfe6ea,#9a9690 60%,#6d6a64);clip-path:polygon(0 0,460px 0,501px 40px,501px 291px,460px 331px,0 331px)" role="img" aria-label="Supreme Court building facade"></div>
  <div class="insight-photo" style="left:601px;background:linear-gradient(135deg,#7a6450,#20305e 55%,#e8e8ec);clip-path:polygon(41px 0,501px 0,501px 331px,41px 331px,0 291px,0 40px)" role="img" aria-label="Attorneys reviewing a claim with a client"></div>
  <div class="abs play"><svg width="14" height="16" viewBox="0 0 14 16"><path d="M2 1l11 7-11 7z" fill="#fff"/></svg></div>
  <h3 class="insight-caption" style="left:92px">What is an MDL and how does it work?</h3>
  <h3 class="insight-caption" style="left:601px">What happens after you submit a claim?</h3>
  <a class="btn btn-outline" style="left:248px;top:2655px;width:179px;height:43px">Read Our Blog</a>
  <a class="btn btn-outline" style="left:742px;top:2655px;width:179px;height:43px">Watch Our Videos</a>
</section>

<!-- ongoing -->
<section>
  <div class="abs ongoing-frame"></div>
  <div class="photo ongoing-photo" role="img" aria-label="Group of people signing claim documents at a table"></div>
  <h2 class="abs ongoing-title">ONGOING MDLS &amp; CLASS<br>ACTION INVESTIGATIONS</h2>
  <p class="abs ongoing-copy">We're currently investigating and accepting claims for several high-impact legal matters. If you think you may qualify, reach out today for a free consultation.</p>
  <ul class="abs ongoing-list">
    <li><svg width="11" height="11" viewBox="0 0 11 11"><circle cx="5.5" cy="5.5" r="5.5" fill="#1aa5f6"/><path d="M3 5.6l1.7 1.6L8 4" stroke="#fff" stroke-width="1.3" fill="none"/></svg>Drug &amp; Medical Device MDLs</li>
    <li><svg width="11" height="11" viewBox="0 0 11 11"><circle cx="5.5" cy="5.5" r="5.5" fill="#1aa5f6"/><path d="M3 5.6l1.7 1.6L8 4" stroke="#fff" stroke-width="1.3" fill="none"/></svg>Defective Consumer Products</li>
    <li><svg width="11" height="11" viewBox="0 0 11 11"><circle cx="5.5" cy="5.5" r="5.5" fill="#1aa5f6"/><path d="M3 5.6l1.7 1.6L8 4" stroke="#fff" stroke-width="1.3" fill="none"/></svg>Toxic Exposure Cases</li>
    <li><svg width="11" height="11" viewBox="0 0 11 11"><circle cx="5.5" cy="5.5" r="5.5" fill="#1aa5f6"/><path d="M3 5.6l1.7 1.6L8 4" stroke="#fff" stroke-width="1.3" fill="none"/></svg>Data Breach Class Actions</li>
  </ul>
  <a class="btn btn-solid" style="left:638px;top:3104px;width:208px;height:42px">See Active Investigations</a>
</section>

<!-- footer band + cta -->
<div class="abs footer-band"></div>
<section class="abs cta">
  <svg class="abs" style="left:0;top:0" width="1005" height="221" viewBox="0 0 1005 221">
    <polygon points="560,221 680,0 740,0 620,221" fill="#0a1a8a" opacity=".9"/>
    <polygon points="870,221 990,0 1005,0 1005,40 905,221" fill="#0a1a8a"/>
  </svg>
  <div class="abs" style="left:630px;top:0;width:330px;height:221px;background:linear-gradient(180deg,#8a7868,#c9a388 45%,#1b2236);clip-path:polygon(110px 0,330px 0,220px 221px,0 221px)" role="img" aria-label="Smiling attorney in a dark blazer"></div>
  <h2 class="abs cta-title">Let's discuss your case<br>no cost, no obligation</h2>
  <p class="abs cta-copy">Our legal consultations are free, confidential, and designed to give you clear direction. Take the first step today.</p>
  <a class="btn btn-navy" style="left:62px;top:145px;width:244px;height:42px">Schedule a Free Consultation</a>
</section>

<footer>
  <div class="logo" style="left:99px;top:3630px;background:var(--white);padding:8px 14px;width:267px;height:46px">
    <span class="logo-mark" style="width:30px;height:30px"></span>
    <span class="logo-name" style="font-size:16px">THORNFIELD MARSH, LLC</span>
  </div>
  <nav class="abs footer-nav"><span>Home</span><span>About</span><span>Legal Team</span><span>MDLs</span><span>Blog</span><span>Contact</span></nav>
  <div class="abs footer-rule-left"></div>

  <h3 class="abs contact-title">Contact Info</h3>
  <ul class="abs contact-list">
    <li>Thornfield &amp; Marsh Law Group</li>
    <li><svg width="10" height="10" viewBox="0 0 10 10"><path d="M2 1l2 2-1 1.5c.7 1.3 1.3 1.9 2.5 2.5L7 6l2 2-1.2 1.5C4.5 9 1 5.5.5 2.2z" fill="#1aa5f6"/></svg>Phone: (xxx) xxx-xxxx</li>
    <li><svg width="10" height="8" viewBox="0 0 10 8"><rect width="10" height="8" fill="#1aa5f6"/><path d="M0 0l5 4 5-4" stroke="#0a1a8a" fill="none"/></svg>Email: info@thornfieldmarshlaw.com</li>
    <li><svg width="9" height="11" viewBox="0 0 9 11"><path d="M4.5 0A4 4 0 0 0 .5 4c0 3 4 7 4 7s4-4 4-7a4 4 0 0 0-4-4z" fill="#1aa5f6"/><circle cx="4.5" cy="4" r="1.4" fill="#0a1a8a"/></svg>Office Location: [Address]</li>
  </ul>

  <span class="social" style="left:934px"></span>
  <span class="social" style="left:978px"></span>
  <span class="social" style="left:1021px"></span>
  <span class="social" style="left:1059px"></span>

  <a class="abs to-top"><svg width="12" height="8" viewBox="0 0 12 8"><path d="M1 7l5-5 5 5" stroke="#fff" stroke-width="1.6" fill="none"/></svg></a>
  <div class="abs footer-rule"></div>
  <p class="abs legal">This website is for informational purposes only and does not constitute legal advice. Viewing this site or submitting information does not create an attorney-client relationship.<br>© 2025 Thornfield &amp; Marsh Law Group. All rights reserved.</p>
</footer>

</body>
</html>
```